TRNV LLP website - revamping our website after 23 years

Our website needs a complete overhaul. The purpose of this exercise is to provide us with your vision of what you think the website should look like. We don't need the website to be created or coded. Just need creative designs.

We have a four sites that we would like to base our website on;

We like the simplicity of Fairwicks, the style of Pemberly Strand and Kettridge.

http://www.pemberlystrand-example.com/en/toronto-ontario/
http://www.fairwicks-example.ca/
hallkettridge-example.com
http://www.vendrupe-example.com/our-professionals.html

We have a logo that we would like to use which will be attached below. We need to keep our website looking very professional as we have a large number of high net worth clients.
Updates

Hi, We've received some good website designs but they appear to be the same type of template websites we've received in the past - this is not what we're looking for. What we want is a unique website that is modelled on the following three company websites: http://www.fairwicks-example.ca/ www.hallkettridge-example.com/ http://www.pemberlystrand-example.com/en/toronto-ontario/

Thank you everyone for your designs. I will be posting updates and my comments on the various designs in the next day - I want to thank you for the creative designs I see. I thought i would explain a bit about our firm and perhaps it can help when you design the theme of our website: - Our firm is like a family and our clients are truly like our friends. We have close knit relationships in and outside of the office with staff and clients. - We are an 'out of the box' type of firm. We operate differently than most firms and that's a differentiating factor in what makes us who we are - Our slogan is "Count on us" which is a testament to the way we run our practice - We would like an open, fresh, clean look to our website - we don't want the landing page to be overly long or complex because we have limited time to update the website and limited content That's it for the time being - when things come to mind I will post them here.

Can we try a design as follows: - make the website look very similar to www.fairwicks-example.ca - use the same background colour - Keep the same black top but insert our logo - incorporate some of the content from our current website www.trnv-example.com

I have been away dealing with a personal matter. I will look into these websites tomorrow afternoon and provide more feedback / info on the top designer. Thank you

Hi designers, I want to apologize for the delay. I plan on wrapping things up within the next few days. I will go through a few of the top designs and offer my comments. Thank you for your patience.

Target Market(s)

Mainly our current clients - We have a large number of high net worth individuals as clients.

Industry/Entity Type

Accounting

Number of Pages Required

1 page

Requirements
Must have
• Please model website on the websites indicated above.
• Our current website is www.trnv-example.com. It's dark, cluttered and not inviting. We want a fresh, clean website. Please incorporate the logo's attached below.

```html
<!DOCTYPE html>
<html lang="en">
<head>
<meta charset="utf-8">
<title>TRNV LLP — Chartered Accountants</title>
<link rel="stylesheet" href="https://fonts.googleapis.com/css2?family=Noto+Serif&family=Open+Sans:wght@400;600&display=swap">
<style>
:root{
  --header:#2b2b2b;
  --maroon:#8a1c50;
  --blue:#27a3dc;
  --ice:#e4ecf1;
  --text:#555;
  --heading:#2f2f2f;
  --footer:#0c0c0d;
  --footer-deep:#121213;
  --muted:#9a9a9a;
}
*{margin:0;padding:0;box-sizing:border-box}
html,body{width:775px;height:1200px;overflow:hidden;background:#fff}
body{position:relative;font-family:"Open Sans",Arial,sans-serif;color:var(--text)}
.abs{position:absolute}
.serif{font-family:"Noto Serif",Georgia,serif;font-weight:400}

/* header */
.site-header{left:0;top:0;width:775px;height:87px;background:var(--header);border-bottom:1px solid #555}
.brand{left:72px;top:54px;font-size:20px;color:#c9c9c9;letter-spacing:.5px}
.brand-mark{left:100px;top:14px;width:30px;height:30px;border-radius:50%;background:#5a5a5a}
.search{left:572px;top:18px;width:131px;height:24px;background:#3a3a3a;border:1px solid #444;font-size:7px;color:#999;padding:7px 9px}
.search svg{position:absolute;right:7px;top:7px}
.main-nav{left:0;top:65px;width:775px;height:22px}
.main-nav a{position:absolute;top:0;font-size:7.5px;color:#e9e9e9;text-decoration:none;letter-spacing:.2px}
.main-nav a.active{color:var(--blue);font-weight:600}
.nav-marker{left:288px;top:84px;width:25px;height:3px;background:var(--blue)}

/* hero */
.hero{left:0;top:87px;width:775px;height:318px;background:linear-gradient(100deg,#d9dadb 0%,#bdbcbc 30%,#8f8478 55%,#3d4350 80%,#2a2f3c 100%)}
.hero-arrow{top:238px}
.hero-card{left:72px;top:223px;width:330px;height:148px;background:rgba(255,255,255,.82);padding:18px 25px}
.hero-card h1{font-size:20px;color:var(--heading);margin-bottom:6px}
.hero-card p{font-size:7px;line-height:17px;color:#444}
.btn{display:inline-block;background:var(--maroon);color:#fff;font-size:9px;font-weight:600;text-align:center;border-radius:2px}
.hero-card .btn{margin-top:6px;width:114px;height:32px;line-height:32px}

/* feature panels */
.panel-left{left:0;top:405px;width:388px;height:155px;background:var(--ice)}
.panel-left .photo{left:0;top:0;width:150px;height:155px;background:linear-gradient(90deg,#f1f1f0,#d9dde2 80%,var(--ice))}
.panel-right{left:388px;top:405px;width:387px;height:155px;background:var(--blue)}
.panel-right .photo{left:232px;top:0;width:155px;height:155px;background:linear-gradient(90deg,var(--blue),#6c8fae 60%,#3f5875)}
.feature{position:absolute}
.feature h2{font-size:14px;line-height:20px}
.feature p{font-size:7px;line-height:17px;margin-top:6px}
.feature .more{font-size:9.5px;font-weight:600;text-decoration:none;display:flex;align-items:center;gap:3px}
.panel-left .feature{left:156px;top:33px;width:215px;color:#666}
.panel-left h2{color:var(--heading)}
.panel-left .more{color:var(--maroon);margin-top:8px}
.panel-right .feature{left:32px;top:28px;width:215px;color:#fff}
.panel-right .more{color:#fff;margin-top:14px}

/* about */
.about-title{left:71px;top:594px;font-size:14px;color:var(--heading)}
.about-copy{left:71px;top:613px;width:408px;font-size:7px;line-height:20px;color:#777}
.about .btn{left:71px;top:699px;width:82px;height:33px;line-height:33px}
.about-photo{left:494px;top:594px;width:209px;height:139px;border:3px solid #fff;box-shadow:0 0 0 1px #ccc;background:linear-gradient(180deg,#d8e3ec,#b9c6d2 45%,#39414d)}

/* news */
.news{left:0;top:752px;width:775px;height:258px;background:#e5edf2}
.news h2{position:absolute;left:0;top:30px;width:775px;text-align:center;font-size:14px;color:var(--heading)}
.tabs{left:71px;top:63px;width:631px;height:45px;display:flex;border:1px solid #dde2e6}
.tab{flex:1;text-align:center;line-height:45px;font-size:10px;color:#333;background:linear-gradient(#fff,#e6e6e6);border-left:1px solid #ddd}
.tab.active{flex:0 0 181px;background:var(--blue);color:#fff;border-left:0;position:relative}
.tab.active::after{content:"";position:absolute;left:86px;bottom:-6px;border:6px solid transparent;border-bottom:0;border-top-color:var(--blue)}
.news-item{position:absolute;top:135px;width:310px}
.news-thumb{position:absolute;left:0;top:2px;width:129px;height:85px;border:3px solid #fff;box-shadow:0 0 0 1px #ccc}
.news-body{position:absolute;left:141px;top:0;width:166px}
.news-body h3{font-size:8.5px;font-weight:400;line-height:13px;color:#444}
.news-date{font-size:7px;color:#555;margin:9px 0 5px;display:flex;align-items:center;gap:2px}
.news-body p{font-size:6.5px;line-height:13.5px;color:#888;text-align:justify}
.news-arrow{top:172px}

/* footer */
.site-footer{left:0;top:1010px;width:775px;height:140px;background:var(--footer)}
.cover{left:72px;top:20px;width:101px;height:101px;background:linear-gradient(180deg,#1d3d55,#2a5a74 60%,#9fb7c5)}
.rule{top:16px;width:1px;height:120px;background:#2a2a2a}
.foot-col{position:absolute;top:22px}
.foot-col h4{font-size:11px;color:#eee;margin-bottom:8px}
.foot-col li{list-style:none;font-size:7.5px;color:#aaa;line-height:20px}
.foot-col p{font-size:6.5px;color:#999;line-height:13px;width:200px}
.email{width:213px;height:26px;background:#fff;border-radius:2px;margin-top:11px;font-size:6.5px;color:#aaa;padding:8px 9px}
.subscribe{margin-top:4px;width:76px;height:22px;line-height:22px;font-size:7px}
.bottom-bar{left:0;top:1150px;width:775px;height:50px;background:var(--footer-deep);text-align:center;font-size:7px;color:var(--muted);line-height:50px}
.bottom-bar a{color:var(--blue);text-decoration:none;font-weight:600}
</style>
</head>
<body>

<header class="site-header abs">
  <div class="brand abs serif">TRNV LLP</div>
  <div class="search abs">Search...
    <svg width="9" height="9" viewBox="0 0 10 10"><circle cx="4" cy="4" r="3" fill="none" stroke="#aaa" stroke-width="1.3"/><line x1="6.3" y1="6.3" x2="9" y2="9" stroke="#aaa" stroke-width="1.3"/></svg>
  </div>
  <nav class="main-nav abs">
    <a class="active" style="left:302px">HOME</a>
    <a style="left:354px">ABOUT TRNV</a>
    <a style="left:428px">SERVICES</a>
    <a style="left:491px">LIBARY</a>
    <a style="left:546px">LINKS</a>
    <a style="left:598px">CAREERS</a>
    <a style="left:659px">CONTACT US</a>
  </nav>
</header>
<div class="nav-marker abs" style="left:288px;width:26px"></div>

<section class="hero abs" role="img" aria-label="Photo of two businessmen discussing documents at a desk">
</section>
<svg class="hero-arrow abs" style="left:25px" width="12" height="18" viewBox="0 0 12 18"><polyline points="10,2 3,9 10,16" fill="none" stroke="rgba(255,255,255,.7)" stroke-width="3"/></svg>
<svg class="hero-arrow abs" style="left:740px" width="12" height="18" viewBox="0 0 12 18"><polyline points="2,2 9,9 2,16" fill="none" stroke="rgba(255,255,255,.8)" stroke-width="3"/></svg>
<div class="hero-card abs">
  <h1 class="serif">WELCOME TO TRNV</h1>
  <p>Donec ut magna vel nisi suscipit pellentesque. Sed rutrum, libero et consectetur porttit or, ipsum ante aliquam velit, eu sollicitudin dolor diam ac sapien. Maecenas suscipit, nulla quis vehicula interdum, turpis tortor.sem.</p>
  <span class="btn">GET IN TOUCH</span>
</div>

<section class="panel-left abs">
  <div class="photo abs" role="img" aria-label="Photo of a hand writing with a gold pen"></div>
  <div class="feature">
    <h2 class="serif">2015 TAX ESTIMATOR FOR 2014 NOW ONLINE !</h2>
    <p>Lorem ipsum dolor sit amet, consectetuer adipiscing elit, sed diam nonummy nibh euismod tincidunt ut laoreet dolore.</p>
    <a class="more"><svg width="9" height="9" viewBox="0 0 10 10"><circle cx="5" cy="5" r="5" fill="currentColor"/><polyline points="4,2.8 6.2,5 4,7.2" fill="none" stroke="#e4ecf1" stroke-width="1.4"/></svg>CLICK MORE DETAILS</a>
  </div>
</section>
<section class="panel-right abs">
  <div class="photo abs" role="img" aria-label="Photo of a handshake in front of office towers"></div>
  <div class="feature">
    <h2 class="serif">TRNV TAX TIPS</h2>
    <p>Cras malesuada tellus at lectus gravida consequat. Nunc turpis justo, vestibulum id dui non, ultricies vehicula neque. Sed egestas facilisis libero, vel convallis mauris.</p>
    <a class="more"><svg width="9" height="9" viewBox="0 0 10 10"><circle cx="5" cy="5" r="5" fill="#fff"/><polyline points="4,2.8 6.2,5 4,7.2" fill="none" stroke="#27a3dc" stroke-width="1.4"/></svg>CLICK MORE DETAILS</a>
  </div>
</section>

<section class="about">
  <h2 class="about-title abs serif">WHO WE ARE?</h2>
  <p class="about-copy abs">Lorem ipsum dolor sit amet, consectetur adipiscing elit. Ut sed libero felis. In consequat iaculis urna a viverra. Aliquam posuere, mi sit amet semper tristique, mauris magna hendrerit libero, volutpat sollicitudin enim turpis volutpat metus. In fermentum, lorem dictum accumsan blandit, risus elit fermentum felis, ac aliquam justo leo non nulla. In maximus justo ut nisi blandit, in pretium orci porta.</p>
  <span class="btn abs">READ MORE</span>
  <div class="about-photo abs" role="img" aria-label="Photo of the firm's team standing together in an office"></div>
</section>

<section class="news abs">
  <h2 class="serif">TRNV NEWS</h2>
  <div class="tabs abs">
    <div class="tab active">SEP 2015</div>
    <div class="tab">OCT 2015</div>
    <div class="tab">NOV 2015</div>
    <div class="tab">DEC 2015</div>
  </div>
  <svg class="news-arrow abs" style="left:32px" width="15" height="15" viewBox="0 0 16 16"><circle cx="8" cy="8" r="8" fill="#b5b9bc"/><polyline points="9.5,4.5 6,8 9.5,11.5" fill="none" stroke="#fff" stroke-width="2"/></svg>
  <svg class="news-arrow abs" style="left:724px" width="15" height="15" viewBox="0 0 16 16"><circle cx="8" cy="8" r="8" fill="#b5b9bc"/><polyline points="6.5,4.5 10,8 6.5,11.5" fill="none" stroke="#fff" stroke-width="2"/></svg>
  <article class="news-item" style="left:76px">
    <div class="news-thumb" role="img" aria-label="Photo of a magnifying glass over financial charts" style="background:linear-gradient(135deg,#5b6677,#a38a5e 50%,#e8ecf1)"></div>
    <div class="news-body">
      <h3>Ut wisi enim ad minim veniam, quis nostr ud exerci tation ullamcorper</h3>
      <div class="news-date"><svg width="7" height="7" viewBox="0 0 8 8"><rect x="0" y="1" width="8" height="7" fill="#8a1c50"/><rect x="1" y="3" width="6" height="4" fill="#e5edf2"/></svg>13 SEP 2015</div>
      <p>Duis autem vel eum iriure dolor in hendrerit in vulputate velit esse molestie consequat, vel illum dolore eu feugiat nulla facilisis...</p>
    </div>
  </article>
  <article class="news-item" style="left:397px">
    <div class="news-thumb" role="img" aria-label="Photo of a tax form with pencils and a calculator" style="background:linear-gradient(135deg,#ddd7cc,#cfc8bb 50%,#4b5f86)"></div>
    <div class="news-body">
      <h3>Lorem ipsum dolor sit amet, consectetur adipiscing elit.</h3>
      <div class="news-date"><svg width="7" height="7" viewBox="0 0 8 8"><rect x="0" y="1" width="8" height="7" fill="#8a1c50"/><rect x="1" y="3" width="6" height="4" fill="#e5edf2"/></svg>12 SEP 2015</div>
      <p>Nunc turpis justo, vestibulum id dui non, ultricies vehicula neque. Sed egestas facilisis libero, vel convallis mauris fermentum nec.</p>
    </div>
  </article>
</section>

<footer class="site-footer abs">
  <div class="cover abs" role="img" aria-label="Cover of the firm's personal tax commentary booklet"></div>
  <div class="rule abs" style="left:203px"></div>
  <div class="rule abs" style="left:328px"></div>
  <div class="rule abs" style="left:453px"></div>
  <div class="foot-col" style="left:231px">
    <h4 class="serif">INFORMATION</h4>
    <ul><li>About</li><li>Testimonials</li><li>Programs</li><li>Links</li></ul>
  </div>
  <div class="foot-col" style="left:353px">
    <h4 class="serif">QUICK LINKS</h4>
    <ul><li>Privacy Policy</li><li>Services</li><li>Blog</li><li>Contact Us</li></ul>
  </div>
  <div class="foot-col" style="left:489px">
    <h4 class="serif">NEWSLETTER SIGNUP</h4>
    <p>Enter your email address to receive our latest newsletters containing our latest News.</p>
    <div class="email">Email Address</div>
    <div class="btn subscribe">SUBSCRIBE</div>
  </div>
</footer>
<div class="bottom-bar abs">TRNV Chartered Accountants &nbsp;© 2015. <a>Disclaimer</a></div>

</body>
</html>
```